Design a PRODUCT TAG for backpackers and travellers equipment/accessories company

We need a Tag Design for our products. We are a new company based in the UK called 'RoamNest'. We produce travel equipment and accessories for backpackers. Our customers are young (18-30) individuals usually GAP year makers or young professionals who enjoy travelling, adventures and exploring the world. The Tag must state our name RoamNest (at the front) and Logo(at the front) and website address www.roamnest-example.uk (on the back) and communicate our company's aim of making backpackers trip hassle free where full attention is concentrated on adventure and fun.

Target Market(s)

Young individual passionate about travelling. 18-30 age. UNI students, gap year makers or young professionals

Industry/Entity Type

Travel Industry

Colors
3276b5
33a6d7
33b8a4
abd036
fbee3d
fece3e
f68d4d
0592cd
85cae6

Requirements
Must have
• The logo and on the front
• The web address at the back
• Half of the back should be black in order to fit the product label
Nice to have
• Would be nice for the design to look like something related to travel, so for example like a plain ticket, or passport, or anything else that can be related to holiday making and travelling.

```html
<!DOCTYPE html>
<html lang="en">
<head>
<meta charset="utf-8">
<title>RoamNest Product Tag</title>
<link rel="stylesheet" href="https://fonts.googleapis.com/css2?family=Jost:wght@600;700&family=Lobster&display=swap">
<style>
  :root {
    --tag-yellow: #f5ef3f;
    --brand-blue: #2f78bd;
    --scene-teal: #25b8a0;
    --page: #ffffff;
  }
  html, body {
    margin: 0;
    padding: 0;
    overflow: hidden;
    background: var(--page);
  }
  .canvas {
    position: relative;
    width: 1200px;
    height: 848px;
    background: var(--page);
    overflow: hidden;
  }
  .tag {
    position: absolute;
    width: 368px;
    height: 600px;
    overflow: visible;
  }
  .tag--front { left: 140px; top: 94px; }
  .tag--back  { left: 721px; top: 85px; }
  .tag-body { fill: var(--tag-yellow); }
  .tag-hole { fill: var(--page); }
  .front-title {
    font-family: "Jost", sans-serif;
    font-weight: 700;
    font-size: 56px;
    letter-spacing: 10px;
    fill: var(--brand-blue);
  }
  .badge-ring {
    fill: none;
    stroke: var(--brand-blue);
    stroke-width: 3;
  }
  .badge-name {
    font-family: "Jost", sans-serif;
    font-weight: 700;
    font-size: 50px;
    fill: var(--brand-blue);
  }
  .slogan {
    font-family: "Lobster", cursive;
    font-size: 62px;
    letter-spacing: 2px;
    fill: var(--brand-blue);
  }
  .web-address {
    font-family: "Jost", sans-serif;
    font-weight: 700;
    font-size: 18px;
    letter-spacing: 3px;
    fill: var(--brand-blue);
  }
</style>
</head>
<body>
<main class="canvas">

  <svg class="tag tag--front" viewBox="0 0 368 600" aria-label="Tag front">
    <path class="tag-body" d="M0 0 H368 V416 A184 184 0 0 1 0 416 Z"/>
    <circle class="tag-hole" cx="184" cy="46" r="20"/>
    <text class="front-title" x="189" y="139" text-anchor="middle">ROAM</text>
    <text class="front-title" x="189" y="215" text-anchor="middle">NEST</text>
    <circle class="badge-ring" cx="184" cy="411" r="168"/>
    <text class="badge-name" x="184" y="428" text-anchor="middle">RoamNest</text>
  </svg>

  <svg class="tag tag--back" viewBox="0 0 368 600" aria-label="Tag back">
    <defs>
      <clipPath id="back-shape">
        <path d="M0 0 H368 V416 A184 184 0 0 1 0 416 Z"/>
      </clipPath>
      <linearGradient id="scene-fade" x1="0" y1="0" x2="0" y2="1">
        <stop offset="0" stop-color="#25b8a0" stop-opacity="0"/>
        <stop offset="0.45" stop-color="#25b8a0" stop-opacity="0.55"/>
        <stop offset="1" stop-color="#25b8a0"/>
      </linearGradient>
    </defs>
    <path class="tag-body" d="M0 0 H368 V416 A184 184 0 0 1 0 416 Z"/>
    <circle class="tag-hole" cx="184" cy="46" r="20"/>

    <g clip-path="url(#back-shape)">
      <rect x="0" y="410" width="368" height="190" fill="url(#scene-fade)"
            role="img" aria-label="Landscape silhouette with palm trees, islands, pines, mountains and aeroplanes on dotted flight routes"/>
    </g>

    <text class="slogan" x="186" y="126" text-anchor="middle">Adventure</text>
    <text class="slogan" x="186" y="201" text-anchor="middle">Awaits...</text>
    <text class="slogan" x="186" y="285" text-anchor="middle">GO</text>
    <text class="slogan" x="186" y="352" text-anchor="middle">Find it</text>
    <text class="web-address" x="186" y="381" text-anchor="middle">www.roamnest-example.uk</text>
  </svg>

</main>
</body>
</html>
```